Creative Businesss Card desgin!

Create a business card for our business Gleam window cleaning!
We are open to creative ideas as long as it maintains a professional image.

Target Market(s)

Small Commercial window cleaning clients including car dealerships, strata manager, cafe

Industry/Entity Type

Window Cleaning

Contact Information for Business Card

Daniel Prescott
General Manager
Gleam Window Cleaning

daniel@gleamservices.com.au
pane-care-southbank.com.au
Ph: 1800 GET GLEAM
Mob: 0437 582 061

Colors
fbed22
0392cd

Requirements
Should not have
• Stock window cleaning/ squeegee graphics

```html
<!DOCTYPE html>
<html lang="en">
<head>
<meta charset="utf-8">
<title>Gleam Window Cleaning – Business Card</title>
<link href="https://fonts.googleapis.com/css2?family=Arimo:wght@400;700&display=swap" rel="stylesheet">
<style>
  :root {
    --brand-blue: #0d578a;
    --brand-yellow: #f2ea2a;
    --backdrop: #2b2b2d;
  }
  * { box-sizing: border-box; margin: 0; padding: 0; }
  html, body {
    width: 1200px; height: 880px; overflow: hidden;
    background: var(--backdrop);
    font-family: "Arimo", Arial, sans-serif;
  }
  .canvas {
    width: 1200px; height: 880px;
    display: flex; flex-direction: column;
    align-items: center; justify-content: center; gap: 44px;
  }
  .card {
    position: relative;
    width: 640px; height: 366px;
    background: var(--brand-blue);
    border-radius: 22px;
    overflow: hidden;
    color: var(--brand-yellow);
  }
  .card-front .accent-band {
    position: absolute; left: 110px; top: 0;
    width: 150px; height: 100%;
    background: var(--brand-yellow);
  }
  .wordmark {
    position: absolute; right: 56px;
    text-align: left;
    font-weight: 700; color: var(--brand-yellow);
    line-height: 1;
  }
  .card-front .wordmark { top: 150px; }
  .card-back .wordmark { top: 56px; }
  .wordmark .name { display: block; font-size: 66px; letter-spacing: 2px; }
  .wordmark .tagline { display: block; font-size: 19px; letter-spacing: 1px; margin-top: 4px; padding-left: 36px; }

  .person {
    position: absolute; left: 36px; top: 232px;
  }
  .person .full-name { font-size: 21px; font-weight: 700; line-height: 1.05; }
  .person .role { font-size: 17px; font-weight: 400; line-height: 1.1; }

  .divider {
    position: absolute; left: 36px; right: 36px; top: 284px;
    height: 2px; background: var(--brand-yellow);
  }
  .contacts {
    position: absolute; left: 36px; right: 36px; top: 296px;
    font-size: 15.5px; line-height: 1.45;
  }
  .contact-row { display: flex; align-items: center; white-space: nowrap; }
  .contact-item { display: inline-flex; align-items: center; gap: 6px; }
  .sep { margin: 0 10px; opacity: .9; }
  .icon { width: 13px; height: 13px; flex: none; color: var(--brand-yellow); }
</style>
</head>
<body>
<main class="canvas">

  <section class="card card-front" aria-label="Card front">
    <div class="accent-band"></div>
    <div class="wordmark">
      <span class="name">GLEAM</span>
      <span class="tagline">WINDOW CLEANING</span>
    </div>
  </section>

  <section class="card card-back" aria-label="Card back">
    <div class="wordmark">
      <span class="name">GLEAM</span>
      <span class="tagline">WINDOW CLEANING</span>
    </div>

    <div class="person">
      <p class="full-name">Daniel Prescott</p>
      <p class="role">General Manager</p>
    </div>

    <div class="divider"></div>

    <div class="contacts">
      <div class="contact-row">
        <span class="contact-item">
          <svg class="icon" viewBox="0 0 16 16" aria-hidden="true"><path fill="currentColor" d="M2 5c0-2 2-3 6-3s6 1 6 3v1h-3V5H5v1H2zM4 7h8l2 6H2z"/><circle cx="8" cy="10" r="1.6" fill="#0d578a"/></svg>
          1800 GET GLEAM
        </span>
        <span class="sep">|</span>
        <span class="contact-item">
          <svg class="icon" viewBox="0 0 16 16" aria-hidden="true"><rect x="4" y="1" width="8" height="14" rx="1.5" fill="none" stroke="currentColor" stroke-width="1.6"/><rect x="7" y="12" width="2" height="1.2" fill="currentColor"/></svg>
          0437 582 061
        </span>
        <span class="sep">|</span>
        <span class="contact-item">
          <svg class="icon" viewBox="0 0 16 16" aria-hidden="true"><rect x="1" y="3" width="14" height="10" fill="currentColor"/><path d="M1 3l7 6 7-6" fill="none" stroke="#0d578a" stroke-width="1.4"/></svg>
          daniel@gleamservices.com.au
        </span>
      </div>
      <div class="contact-row">
        <span class="contact-item">
          <svg class="icon" viewBox="0 0 16 16" aria-hidden="true"><circle cx="8" cy="8" r="6.5" fill="none" stroke="currentColor" stroke-width="1.5"/><ellipse cx="8" cy="8" rx="2.8" ry="6.5" fill="none" stroke="currentColor" stroke-width="1.2"/><path d="M1.5 8h13" stroke="currentColor" stroke-width="1.2"/></svg>
          pane-care-southbank.com.au
        </span>
      </div>
    </div>
  </section>

</main>
</body>
</html>
```